VALMIRA/ VALMIRA GREY Business Card

We have two brands that we would like to show one 1 business card (front and back). We would to incorporate two different logos on one card (VALMIRA and VALMIRA GREY). Card can be two sided. Simple, sleek and professional.

We are a senior living provider.

www.valmira-example.com
www.valmiragrey-example.com

Target Market(s)

Professionals

Industry/Entity Type

Business

Font styles to use
Serif

Colors

Designer to choose colors to be used in the design.

Requirements
Must have
• Space for EMAIL, PHONE, WEBSITE
Nice to have
• Raised lettering or gloss lettering

```html
<!DOCTYPE html>
<html lang="en">
<head>
<meta charset="utf-8">
<title>VALMIRA / VALMIRA GREY Business Card</title>
<link rel="stylesheet" href="https://fonts.googleapis.com/css2?family=Arimo&family=Cinzel:wght@400;500&display=swap">
<style>
  :root {
    --gold: #d1a651;
    --ink: #1f201f;
    --charcoal: #232323;
    --graphite: #3d3c3b;
    --paper: #ffffff;
    --mist: #ececec;
    --serif: "Cinzel", "Times New Roman", serif;
    --sans: "Arimo", Arial, sans-serif;
  }
  html, body {
    margin: 0;
    padding: 0;
    width: 1034px;
    height: 1200px;
    overflow: hidden;
    background: var(--paper);
  }
  .sheet {
    position: relative;
    width: 1034px;
    height: 1200px;
  }
  .card {
    position: absolute;
    left: 0;
    width: 1034px;
    height: 592px;
    display: block;
  }
  .card--front { top: 0; }
  .card--back { top: 608px; }

  .brand-name {
    font-family: var(--serif);
    font-weight: 400;
  }
  .brand-name--front { fill: var(--gold); font-size: 96px; letter-spacing: 2px; }
  .brand-name--back { fill: var(--ink); font-size: 54px; letter-spacing: 1px; }
  .tagline { font-family: var(--sans); font-size: 25px; fill: var(--ink); }
  .contact { font-family: var(--sans); font-size: 37px; }
  .contact--dark { fill: var(--ink); }
  .contact--light { fill: var(--paper); }
  .web { font-family: var(--sans); fill: var(--ink); }
  .web--front { font-size: 36px; }
  .web--back { font-size: 31px; }
  .accent-tab { fill: var(--gold); }
  .brand-square { fill: var(--gold); }
</style>
</head>
<body>
<main class="sheet">

  <!-- Front side: VALMIRA -->
  <svg class="card card--front" viewBox="0 0 1034 592" xmlns="http://www.w3.org/2000/svg" aria-label="VALMIRA business card, front">
    <defs>
      <linearGradient id="facet-light-right" x1="1" y1="0" x2="0" y2="1">
        <stop offset="0" stop-color="#dcdcdc"/>
        <stop offset="1" stop-color="#ffffff"/>
      </linearGradient>
      <linearGradient id="facet-light-left" x1="0" y1="0" x2="1" y2="0">
        <stop offset="0" stop-color="#dcdcdc"/>
        <stop offset="1" stop-color="#ffffff"/>
      </linearGradient>
    </defs>
    <rect width="1034" height="592" fill="var(--paper)"/>
    <path class="header-swoosh" d="M0,0 H782 C745,120 640,288 430,300 H0 Z" fill="var(--ink)"/>
    <polygon role="img" aria-label="Geometric faceted line pattern" points="790,0 1034,0 1034,491 680,491 770,360 800,200" fill="url(#facet-light-right)"/>
    <polygon role="img" aria-label="Geometric faceted line pattern" points="0,456 120,470 260,510 395,585 395,592 0,592" fill="url(#facet-light-left)"/>

    <rect class="brand-square" x="28" y="110" width="72" height="72"/>
    <text class="brand-name brand-name--front" x="122" y="182">VALMIRA</text>

    <text class="contact contact--dark" x="26" y="389">Email:xxxxxxxxxxxxxxxx</text>
    <text class="contact contact--dark" x="26" y="438">Phone:xxxxxxxxxxxxxxx</text>

    <path class="accent-tab" d="M397,592 C410,530 450,493 515,493 H1034 V592 Z"/>
    <text class="web web--front" x="700" y="557" text-anchor="middle">www.valmira-example.com</text>
  </svg>

  <!-- Back side: VALMIRA GREY -->
  <svg class="card card--back" viewBox="0 0 1034 592" xmlns="http://www.w3.org/2000/svg" aria-label="VALMIRA GREY business card, back">
    <defs>
      <linearGradient id="card-dark" x1="0" y1="0" x2="1" y2="0">
        <stop offset="0" stop-color="var(--charcoal)"/>
        <stop offset="0.45" stop-color="#2c2b2b"/>
        <stop offset="1" stop-color="var(--graphite)"/>
      </linearGradient>
      <linearGradient id="facet-dark-right" x1="1" y1="0" x2="0" y2="1">
        <stop offset="0" stop-color="#5a5958"/>
        <stop offset="1" stop-color="#2e2d2d"/>
      </linearGradient>
      <linearGradient id="facet-dark-left" x1="0" y1="0" x2="1" y2="0">
        <stop offset="0" stop-color="#4a4948"/>
        <stop offset="1" stop-color="#262626"/>
      </linearGradient>
    </defs>
    <rect width="1034" height="592" fill="url(#card-dark)"/>
    <polygon role="img" aria-label="Geometric faceted line pattern" points="790,0 1034,0 1034,491 720,491 770,360 800,200" fill="url(#facet-dark-right)"/>
    <polygon role="img" aria-label="Geometric faceted line pattern" points="0,456 120,470 260,510 395,585 395,592 0,592" fill="url(#facet-dark-left)"/>
    <path class="header-swoosh" d="M0,0 H778 C740,130 640,290 430,296 H0 Z" fill="var(--paper)"/>

    <rect class="brand-square" x="24" y="62" width="150" height="150"/>
    <text class="brand-name brand-name--back" x="198" y="108">VALMIRA GREY</text>
    <text class="tagline" x="200" y="145">Executive Personal Care Services</text>

    <text class="contact contact--light" x="22" y="389">Email:xxxxxxxxxxxxxxxx</text>
    <text class="contact contact--light" x="22" y="438">Phone:xxxxxxxxxxxxxxx</text>

    <path class="accent-tab" d="M395,592 C408,530 450,492 515,492 H1034 V592 Z"/>
    <text class="web web--back" x="735" y="557" text-anchor="middle">https://www.valmiragrey-example.com</text>
  </svg>

</main>
</body>
</html>
```